Bref créative
Brochures for sophisticated nutrition products
Velvet Crest Products
The brochures to be designed should come across richly textured, for someone who likes elite, high quality, luxury products. We will be printing the brochures using foil inks and foil stamped ink, to bring out the colors. There are 6 brochures needed (6 different products). The brochure should bring out the vivid colors of the products themselves as well. When someone holds these brochures in their hands the though that should come to mind is "This must be expensive, high quality products" Please reference files of what the products look like.
Salon & Spa
The target audience is anyone looking to be fit, healthy, happy.
I am open to new ideas on the layouts of brochures, I would consider tri-fold, double folded. 8.5 x 14 should be the size of the brochures.
This is the current layout and feel of the website. You can see the colors of the products here. To get the details of what the content should be, please visit www.qlorbamerica.example and go to the products section. The content there is what we need to use for the brochures.
file 2
file 3
file 4
file 5
Company Logo File
Label for Product called: SOLO chocolate. The bottle color to go on the brochure is black, like the KVR product bottles.
Label for Product called: SOLO vanilla. The bottle color to go on the brochure is black, like the KVR product bottles.
Product called: HoTaru. Additional to this Box are the individual packets that go into it, which will be uploaded in another file.
Product called: HoTaru (Packets).
Image for Product called: KVR.
Image for product called: Flare
Image for product called: PQL
Supplement Facts Content for all products and Brochures
KVR Brochure Content
Flare Brochure Content
SOLO Brochure Content
HoTaru Brochure Content
PQL Brochure Content

```html
<!DOCTYPE html>
<html lang="en">
<head>
<meta charset="utf-8">
<title>Velvet Crest Products – Tri-fold Brochure</title>
<link rel="stylesheet" href="https://fonts.googleapis.com/css2?family=Open+Sans:wght@400;600;700&family=Cinzel:wght@600&display=swap">
<style>
  :root {
    --stage: #d6d6d6;
    --paper: #f4f4f4;
    --paper-shade: #e2e2e2;
    --espresso: #3b302e;
    --espresso-deep: #2a2220;
    --cocoa: #7a4a3a;
    --gold: #c9a24a;
    --ink: #3a3a3a;
    --ink-soft: #6a6a6a;
    --on-dark: #d8d2ce;
  }
  * { box-sizing: border-box; margin: 0; padding: 0; }
  html, body { width: 1200px; height: 838px; overflow: hidden; }
  body {
    background: var(--stage);
    font-family: "Open Sans", Arial, sans-serif;
    color: var(--ink);
    display: flex; align-items: center; justify-content: center;
  }
  .brochure {
    width: 1080px; height: 700px;
    display: grid; grid-template-columns: repeat(3, 1fr);
    box-shadow: 0 10px 30px rgba(0,0,0,.25);
  }
  .panel { position: relative; height: 100%; overflow: hidden; }
  .panel--light { background: linear-gradient(160deg, var(--paper) 0%, var(--paper-shade) 100%); }

  /* Inside flap: about */
  .about { padding: 70px 40px 0 40px; }
  .about__title { font-size: 15px; font-weight: 700; margin-bottom: 14px; }
  .about__text { font-size: 12.5px; line-height: 1.75; color: var(--ink-soft); margin-bottom: 16px; }
  .about__visual {
    position: absolute; left: 40px; right: 40px; bottom: 40px; height: 190px;
    background: radial-gradient(ellipse at 60% 55%, #3a2a24 0%, #5b4036 40%, #e9e4de 75%, transparent 100%);
    border-radius: 6px;
  }

  /* Back panel: contact */
  .contact {
    background: linear-gradient(180deg, var(--espresso) 0%, var(--espresso-deep) 100%);
    color: var(--on-dark);
    display: flex; flex-direction: column; justify-content: flex-end;
    padding: 0 40px 120px;
    font-size: 12.5px; line-height: 1.8;
  }
  .contact__name { font-weight: 700; margin-bottom: 10px; }
  .contact__group { margin-bottom: 10px; }

  /* Front cover */
  .cover__band {
    height: 80px; background: var(--espresso);
    display: flex; align-items: center; justify-content: flex-end; gap: 12px;
    padding-right: 36px;
  }
  .brand-mark { width: 34px; height: 34px; background: var(--gold); }
  .brand-name {
    font-family: "Cinzel", Georgia, serif; font-weight: 600;
    font-size: 26px; letter-spacing: 3px; color: var(--gold);
  }
  .cover__accent {
    width: 150px; height: 46px;
    background: linear-gradient(90deg, var(--cocoa) 0%, #a26a52 100%);
  }
  .cover__copy { padding: 34px 40px 0 110px; }
  .cover__kicker { font-size: 12.5px; font-weight: 600; margin-bottom: 12px; }
  .cover__headline { font-size: 12.5px; line-height: 1.7; color: var(--ink-soft); }
  .cover__visual {
    position: absolute; left: 60px; right: 30px; bottom: 70px; height: 230px;
    background: radial-gradient(ellipse at 45% 55%, #1f1a18 0%, #4b3a32 35%, #e7a77a 60%, #eef0ea 85%, transparent 100%);
    border-radius: 6px;
  }
</style>
</head>
<body>
  <main class="brochure">
    <section class="panel panel--light about">
      <h2 class="about__title">About Us</h2>
      <p class="about__text">Our nutrition line is made with care for people who want to live well every day. Each formula blends pure ingredients with modern science to support energy, balance and lasting strength for body and mind.</p>
      <p class="about__text">We source only trusted materials and test every batch so you can feel the quality in each serving you take.</p>
      <div class="about__visual" role="img" aria-label="Photo of SOLO chocolate and vanilla tubs with a vanilla shake, strawberry and cocoa"></div>
    </section>

    <section class="panel contact">
      <p class="contact__name">Qlorb International</p>
      <div class="contact__group">
        <p>48 Lindenfall Road</p>
        <p>Suite 12</p>
        <p>Brackwell, NC 00000</p>
      </div>
      <div class="contact__group">
        <p>(555) 010-2040</p>
        <p>(555) 010-2041</p>
        <p>hello@qlorbamerica.example</p>
        <p>www.qlorbamerica.example</p>
      </div>
    </section>

    <section class="panel panel--light cover">
      <header class="cover__band">
        <span class="brand-mark"></span>
        <span class="brand-name">QLORB</span>
      </header>
      <div class="cover__accent"></div>
      <div class="cover__copy">
        <p class="cover__kicker">Health and Wellness</p>
        <p class="cover__headline">What makes this brand the choice for people seeking balance in every area of their lives?</p>
      </div>
      <div class="cover__visual" role="img" aria-label="Photo of two dark product bottles with grapefruit, lemon and fresh herbs"></div>
    </section>
  </main>
</body>
</html>
```